Book Cover for Self Help Book Teens

I need a standard a5 size book cover (front and back) for my new self help book for teens. The book is called
WHEN DAYS DRAG
ideas and tactics for teens in tough times
break ups, school problems, procrastination, fights, sexuality, alcohol, bitchiness, eating problems, can’t sleep, no motivation, not allowed to do stuff, being on the outer..and 34 other common situations that every day Australian teens face
Brenna Faldow
psychologist for teens
I would like a very sparse,very modern cover, no photos - maybe just cartoon-y graphic of smiley face upside down - ie frowny face. Few colours in order to make it look bold. lots of space on the cover.
I will provide back cover text soon
Updates
I just want to say that I really appreciate all of your efforts, the designs were excellent. As a thankyou, I'm happy to email you a link to the e-version of this book if you are interested. Just email me at brennafaldow@quillmarsh.example and I will send it through as soon as it is completed.
Target Market(s)
teens....but parents will also be buying book
Industry/Entity Type
School
Look and feel

```html
<!DOCTYPE html>
<html lang="en">
<head>
<meta charset="utf-8">
<title>When Days Drag — Cover</title>
<link rel="stylesheet" href="https://fonts.googleapis.com/css2?family=Advent+Pro:wght@300;400;500&family=Open+Sans:ital,wght@1,400&family=Nunito:wght@300;400&display=swap">
<style>
  :root {
    --paper: #ffffff;
    --green-deep: #1f7a4a;
    --green-light: #8cc63f;
    --green-mid: #3aa35a;
    --ink-soft: #555555;
    --ink-faint: #b9b9b9;
  }
  html, body {
    margin: 0;
    padding: 0;
    width: 847px;
    height: 1200px;
    overflow: hidden;
    background: var(--paper);
  }
  .cover {
    position: relative;
    width: 847px;
    height: 1200px;
    background: var(--paper);
  }
  .title {
    position: absolute;
    top: 88px;
    left: 0;
    width: 100%;
    margin: 0;
    text-align: center;
    font-family: "Advent Pro", sans-serif;
    font-weight: 400;
    font-size: 96px;
    line-height: 106px;
    letter-spacing: 20px;
  }
  .title span { display: block; padding-left: 20px; }
  .title .word-dark { color: var(--green-deep); }
  .title .word-light { color: var(--green-light); }
  .subtitle {
    position: absolute;
    top: 420px;
    left: 0;
    width: 100%;
    margin: 0;
    text-align: center;
    font-family: "Open Sans", sans-serif;
    font-style: italic;
    font-size: 25px;
    line-height: 36px;
    color: var(--ink-soft);
  }
  .characters {
    position: absolute;
    top: 560px;
    left: 348px;
    width: 152px;
    height: 62px;
  }
  .author {
    position: absolute;
    top: 732px;
    left: 0;
    width: 100%;
    text-align: center;
  }
  .author-name {
    margin: 0;
    font-family: "Advent Pro", sans-serif;
    font-weight: 500;
    font-size: 40px;
    line-height: 44px;
    letter-spacing: 1px;
    color: var(--green-mid);
  }
  .author-role {
    margin: 4px 0 0;
    font-family: "Open Sans", sans-serif;
    font-style: italic;
    font-size: 23px;
    color: var(--ink-soft);
  }
  .topics {
    position: absolute;
    top: 1058px;
    left: 14px;
    width: 822px;
    margin: 0;
    font-family: "Nunito", sans-serif;
    font-weight: 300;
    font-size: 21.5px;
    line-height: 37px;
    color: var(--ink-faint);
  }
  .topics .highlight { color: var(--green-mid); }
</style>
</head>
<body>
  <main class="cover">
    <h1 class="title">
      <span class="word-dark">WHEN</span>
      <span class="word-light">DAYS</span>
      <span class="word-dark">DRAG</span>
    </h1>
    <p class="subtitle">ideas and tactics for<br>teens in tough times</p>

    <svg class="characters" role="img" aria-label="Three small cartoon teen figures with frowning expressions" viewBox="0 0 152 62">
      <rect x="0" y="0" width="152" height="62" rx="10" fill="var(--green-mid)"/>
    </svg>

    <div class="author">
      <p class="author-name">Brenna Faldow</p>
      <p class="author-role">psychologist for teens</p>
    </div>

    <p class="topics">break ups, <span class="highlight">school problems</span>, procrastination, fights, <span class="highlight">sexuality</span>, alcohol, <span class="highlight">bitchiness</span>, eating problems, <span class="highlight">can’t sleep</span>, no motivation, not allowed to do stuff, being on the outer.. and <span class="highlight">34 other</span> common <span class="highlight">situations</span> that every day <span class="highlight">Australian teens</span> face</p>
  </main>
</body>
</html>
```